Freeze dried pet treats and chews packaging design

We are an Belgium based brand selling all natural treats and chews for pets. We are looking for a full color packaging design for a new line of freeze dried treats and chews for cats and dogs. The design should look familiar for our customers with our existing logo, but with a fresh new design especially for this new line. It should reflect our core values of natural, species appropriate food products without any additives or nasties.
The packaging will be a stand-up pouch with zipper, eurohole, easy open and with a window somewhere in the design to show the products inside. Please present your design as a mockup if possible.
Name of the product will be "Velmo Freeze Dried Bitzoos". Add icons to emphasize certain aspects of the product:
- 100% natural
- freeze dried (preserves all nutrients best)
- 100% mono protein
- without additives
- high in protein
- high in flavor
The design is a generic one for 12 different products, only one pouch will be produced and finished with 12 different round labels to indicate the protein source (beef, chicken, lamb, etc). You can include one of these stickers on your design to make the example complete. The sticker should have a separate color for every protein source to make it good distinguishable, an icon representing the protein source (see examples of existing packaging) and a round text around it with the protein source in text in Dutch, French and English (example: RUND - BŒUF - BEEF).
Important: after this design we need more designs for other new product lines, so the winner might get more out of this then only this one project!
High premium pet products
Petfood
- Fontastique, Roboto (used for logo and current designs), others welcome too

```html
<!DOCTYPE html>
<html lang="en">
<head>
<meta charset="utf-8">
<title>Velmo Freeze Dried Bitzoos – Pouch</title>
<link href="https://fonts.googleapis.com/css2?family=Roboto+Condensed:wght@500;700;900&family=Roboto:wght@700&display=swap" rel="stylesheet">
<style>
  :root {
    --stage: #ececec;
    --pouch-white: #f7f7f8;
    --purple: #5b1597;
    --purple-deep: #2e2a6b;
    --green: #7cb82a;
    --green-light: #9acd45;
    --text-white: #ffffff;
    --seal-line: #dcdcde;
  }
  * { box-sizing: border-box; margin: 0; padding: 0; }
  html, body { width: 1200px; height: 835px; overflow: hidden; }
  body {
    background: var(--stage);
    font-family: "Roboto Condensed", "Roboto", sans-serif;
    position: relative;
  }
  .pouch {
    position: absolute;
    left: 420px; top: 98px;
    width: 360px; height: 620px;
    background: var(--pouch-white);
    border-radius: 14px 14px 6px 6px;
    overflow: hidden;
    box-shadow: 0 18px 40px rgba(0,0,0,0.12);
  }
  .seal-top {
    position: absolute; left: 0; top: 0; width: 252px; height: 40px;
    border-bottom: 1px solid var(--seal-line);
  }
  .zipper {
    position: absolute; left: 0; top: 74px; width: 252px; height: 6px;
    border-top: 1px solid var(--seal-line); border-bottom: 1px solid var(--seal-line);
  }
  .euro-hole {
    position: absolute; left: 100px; top: 34px; width: 152px; height: 30px;
    border: 2px solid #c8c8cc; border-radius: 15px; background: #fbfbfb;
  }
  .side-band {
    position: absolute; right: 0; top: 0; width: 108px; height: 100%;
    background: linear-gradient(180deg, var(--green-light), var(--green) 60%, #86c034);
  }
  .band-freeze {
    position: absolute; left: 6px; top: 80px;
    color: var(--text-white); font-weight: 700; font-size: 23px; letter-spacing: 0.5px;
  }
  .band-product {
    position: absolute; left: 18px; top: 108px;
    writing-mode: vertical-rl;
    color: var(--text-white); font-weight: 900; font-size: 52px; letter-spacing: 3px;
    line-height: 1;
  }
  .wave { position: absolute; left: 0; top: 0; width: 252px; height: 300px; }
  .brand-name {
    position: absolute; left: 18px; top: 140px;
    color: var(--text-white);
    font-family: "Roboto", sans-serif; font-weight: 700; font-size: 82px;
    letter-spacing: -1px; line-height: 1;
  }
  .features { position: absolute; left: 30px; top: 292px; list-style: none; }
  .feature { position: relative; height: 51px; width: 160px; }
  .feature-pill {
    position: absolute; left: 24px; top: 13px; width: 136px; height: 26px;
    background: var(--green); border-radius: 0 13px 13px 0;
    color: var(--text-white); font-weight: 700; font-size: 12.5px;
    line-height: 26px; padding-left: 26px; white-space: nowrap;
  }
  .feature-badge {
    position: absolute; left: 0; top: 4px; width: 44px; height: 44px;
    border-radius: 50%; background: var(--purple-deep);
    border: 3px solid var(--green); box-shadow: 0 0 0 2px var(--pouch-white) inset;
  }
</style>
</head>
<body>
  <main class="pouch" aria-label="Velmo Freeze Dried Bitzoos pouch front">
    <div class="seal-top"></div>
    <div class="euro-hole"></div>
    <div class="zipper"></div>

    <svg class="wave" viewBox="0 0 252 300" aria-hidden="true">
      <path d="M0 126 C60 110 110 118 150 132 C190 146 220 140 252 128 L252 262 C200 268 150 262 110 252 C70 242 30 246 0 256 Z" fill="var(--purple)"/>
      <path d="M150 128 C190 130 225 118 252 104 L252 110 C225 124 190 136 150 134 Z" fill="var(--green)"/>
      <path d="M6 282 C40 250 90 246 130 252 C90 252 45 262 6 292 Z" fill="var(--green)"/>
    </svg>

    <h1 class="brand-name">Velmo</h1>

    <ul class="features">
      <li class="feature"><span class="feature-pill">100% Natural</span><span class="feature-badge"></span></li>
      <li class="feature"><span class="feature-pill">High in Protein</span><span class="feature-badge"></span></li>
      <li class="feature"><span class="feature-pill">Without Additives</span><span class="feature-badge"></span></li>
      <li class="feature"><span class="feature-pill">100% Mono Protein</span><span class="feature-badge"></span></li>
      <li class="feature"><span class="feature-pill">High in Flavor</span><span class="feature-badge"></span></li>
      <li class="feature"><span class="feature-pill">Freeze Dried</span><span class="feature-badge"></span></li>
    </ul>

    <aside class="side-band">
      <p class="band-freeze">FREEZE</p>
      <p class="band-product">DRIED BITZOOS</p>
    </aside>
  </main>
</body>
</html>
```